WebDesign | Financial Services Firm - Risk Mitigation

We are a professional services consulting firm that specializes in high net worth individuals over $25,000,000, executives C-suite and above, closely held businesses owners, family offices and highly compensated employees.

Our focus is on risk mitigation and tax efficient strategies. Our clients take their risk on themselves and have a proven track record generating wealth. Our directive is to preserve and protect the wealth they’ve already created.

Our company Harbor Crest Advisory is geared around five directives of asset protection:
1) Legal Structuring
2) Leverage & Financing
3) Risk Management - Asset Protection & Insurance, Trustee Work
4) Asset Management & Investing - Under www.tqlvalemark.com
5) Tax Efficient Strategies

Our Company Mark is a Pentagon with a key in the middle. A pentagon is the most efficient defensive structure. Each point of a pentagon is equal distance front every point . Each side provides support to another and works together, which is the key to our clients success.

Our key colors are blue, black and silver.

We ‘re located in the Pacific Northwest with bi coastal and international clients. We have fewer, higher net worth clients and provide exceptional customer service. We do not do social media.

We'll need the following pages:
-Front Landing Page.
Front page has to have link to hbportal.docuvaultix.com for logging into secure site.
- Contact & About Us Page
- Our Team Page
- Five Sides of Wealth Management
> Legal & Business Structuring
> Leverage & Financing
> Risk Management & Asset Protection.
> Asset Management and Investing - Will link to TQL (won't be turned on for a few months)
> Tax Efficient Strategies.

Industry/Entity Type

Financial Service

Coding

Coded - Design and coding required

Number of Pages Required

5+ page

Font styles to use
Sans Serif

Colors
0555a3

Requirements
Must have
• Our key colors are blue, black and silver.

-Front Landing Page.
- Contact & About Us Page
- Our Team Page
> Leverage & Financing
Nice to have
• I have attached images that have been purchased for use on the webpage. Us or not.

location page: 847 W Alder Ln, Suite 412, Lake Oswego, OR 97035
Should not have
• lots of color.

```html
<!DOCTYPE html>
<html lang="en">
<head>
<meta charset="utf-8">
<title>Harbor Crest Advisory</title>
<link href="https://fonts.googleapis.com/css2?family=Cinzel:wght@400;600&family=Lato:ital,wght@0,400;0,700;1,400&family=Montserrat:ital,wght@0,400;0,500;0,600;0,700;1,700&display=swap" rel="stylesheet">
<style>
:root{
  --navy:#0b2463;
  --blue:#0555a3;
  --sky:#1c8ad6;
  --ink:#222;
  --grey:#777;
  --light:#efefef;
  --mist:#e3e3e3;
  --line:#c9c9c9;
  --white:#fff;
}
*{box-sizing:border-box;margin:0;padding:0}
html,body{width:1200px;height:4630px;overflow:hidden}
body{position:relative;font-family:'Lato',sans-serif;color:var(--ink);background:var(--white)}
.abs{position:absolute}
section,header,footer{position:absolute;left:0;width:1200px}

/* header */
.site-header{top:0;height:126px;background:var(--white)}
.brand{display:flex;align-items:center;gap:12px}
.brand-mark{flex:none;width:34px;height:34px;background:var(--blue)}
.brand-name{font-family:'Montserrat',sans-serif;font-weight:600;font-size:21px;color:var(--navy);letter-spacing:1px;text-transform:uppercase;white-space:nowrap}
.header-brand{left:85px;top:44px}
.call{left:760px;top:52px;display:flex;gap:12px;align-items:center}
.call-icon{width:30px;height:30px;border-radius:50%;background:var(--navy);display:flex;align-items:center;justify-content:center}
.call small{display:block;color:var(--sky);font-size:11px}
.call strong{font-family:'Montserrat',sans-serif;font-size:16px;color:var(--navy);font-weight:500}
.login{left:1022px;top:57px;width:70px;height:30px;background:var(--navy);color:var(--white);font-size:11px;display:flex;align-items:center;justify-content:center;border-radius:2px;text-decoration:none}

.main-nav{position:absolute;top:126px;left:0;width:1200px;height:26px;background:var(--navy)}
.main-nav a{position:absolute;top:0;height:26px;line-height:28px;font-family:'Cinzel',serif;font-size:12px;color:var(--white);text-decoration:none;letter-spacing:.5px}
.main-nav a.active{background:var(--blue);width:90px;text-align:center}
.main-nav a.active::after{content:"";position:absolute;left:36px;bottom:-8px;border:9px solid transparent;border-top-color:var(--blue);border-bottom:0}

/* hero */
.hero{top:152px;height:548px;overflow:hidden}
.hero-photo{position:absolute;inset:0;background:linear-gradient(100deg,#f4f6f9 0%,#eef1f5 38%,#c9d3de 58%,#7f8fa3 78%,#4b5a6f 100%)}
.hero h1{position:absolute;left:82px;top:128px;font-family:'Cinzel',serif;font-weight:400;font-size:37px;line-height:40px;color:var(--navy)}
.hero p{position:absolute;left:89px;top:222px;width:360px;font-size:13px;line-height:17px;color:#333}
.btn{display:flex;align-items:center;justify-content:center;background:var(--blue);color:var(--white);font-size:13px;text-decoration:none}
.hero .btn{position:absolute;left:86px;top:298px;width:148px;height:40px}

/* contact */
.advisory{top:700px;height:490px}
.advisory h2{position:absolute;left:140px;top:115px;font-family:'Montserrat',sans-serif;font-weight:400;font-size:32px;line-height:37px;color:var(--blue)}
.advisory h2 em{font-weight:700}
.advisory .copy{position:absolute;left:145px;top:224px;width:455px;font-size:14px;line-height:17px;color:#222}
.advisory .copy p+p{margin-top:17px}
.field{position:absolute;left:700px;width:345px;height:32px;border:1px solid var(--line);font-size:10px;color:#aaa;padding:9px 12px}
.field sup{color:var(--sky)}
.advisory .btn{position:absolute;left:700px;top:350px;width:148px;height:40px;font-weight:700}

/* services */
.services{top:1190px;height:888px;background:var(--light)}
.sec-title{position:absolute;left:0;width:1200px;text-align:center;font-family:'Montserrat',sans-serif;font-weight:700;font-size:27px;color:var(--navy)}
.sec-title span{color:var(--sky)}
.rule{position:absolute;left:570px;width:60px;height:2px;background:var(--navy)}
.services .intro{position:absolute;left:170px;top:156px;width:860px;text-align:center;font-size:9px;line-height:16px;color:var(--grey)}
.svc{position:absolute;font-family:'Montserrat',sans-serif;font-weight:600;font-size:18px;line-height:21px;color:var(--navy)}
.svc span{display:block;color:var(--sky)}

/* different */
.different{top:2078px;height:525px}
.diff-panel{position:absolute;left:0;top:0;width:598px;height:525px;background:var(--navy)}
.diff-photo{position:absolute;left:598px;top:0;width:602px;height:525px;background:linear-gradient(160deg,#f2f3f4 0%,#dfe2e6 45%,#8d96a3 75%,#3f4b5e 100%)}
.diff-panel h2{position:absolute;left:104px;top:64px;font-family:'Montserrat',sans-serif;font-weight:500;font-size:36px;line-height:38px;color:var(--white)}
.diff-panel h2 strong{display:block;font-size:58px;line-height:56px;color:var(--blue);font-weight:500;letter-spacing:2px}
.checks{position:absolute;left:112px;top:183px;list-style:none;width:380px}
.checks li{display:flex;gap:16px;font-family:'Montserrat',sans-serif;font-size:13px;line-height:16px;color:var(--white);margin-bottom:13px}
.checks svg{flex:none;margin-top:-1px}

/* team */
.team{top:2603px;height:412px}
.member-name{position:absolute;font-family:'Montserrat',sans-serif;font-weight:700;font-size:13px;color:var(--navy)}
.member-bio{position:absolute;width:285px;font-size:8.5px;line-height:15px;color:var(--grey)}
.more{position:absolute;font-size:8px;font-weight:700;color:var(--blue);letter-spacing:.3px}

/* testimonials */
.testimonials{top:3015px;height:550px;background:var(--mist)}
.kicker{position:absolute;left:0;width:1200px;text-align:center;font-family:'Cinzel',serif;font-size:11px;color:var(--sky);letter-spacing:1px}
.sec-head{position:absolute;left:0;width:1200px;text-align:center;font-family:'Montserrat',sans-serif;font-weight:600;font-size:29px;color:var(--navy)}
.quote{position:absolute;background:#f1f1f1;box-shadow:0 2px 8px rgba(0,0,0,.18);text-align:center;font-size:12px;line-height:14px;color:var(--grey)}
.quote b{display:block;position:absolute;left:0;right:0;font-family:'Montserrat',sans-serif;font-size:12px;color:var(--navy);font-weight:600}
.avatar{position:absolute;border-radius:50%;border:3px solid var(--white);box-shadow:0 0 0 2px var(--navy);background:linear-gradient(180deg,#c9a98c,#7a6a5d)}
.arrow-btn{position:absolute;width:22px;height:22px;background:#5d6066;display:flex;align-items:center;justify-content:center}
.dot{position:absolute;top:3472px;width:12px;height:12px;border-radius:50%;border:2px solid var(--blue)}

/* blog */
.blog{top:3565px;height:670px}
.post{position:absolute;top:180px;width:455px;height:310px;background:var(--light)}
.post-photo{position:absolute;left:2px;top:33px;width:216px;height:237px}
.post .meta{position:absolute;left:240px;top:37px;font-size:13px;color:#333}
.post h3{position:absolute;left:240px;top:73px;font-family:'Montserrat',sans-serif;font-weight:500;font-size:20px;line-height:26px;color:var(--blue)}
.post p{position:absolute;left:240px;top:162px;width:185px;font-size:11.5px;line-height:14px;color:var(--grey);text-align:justify}
.post .more{left:240px;top:274px;font-size:12px;color:var(--navy)}

/* footer */
.site-footer{top:4235px;height:355px;background:var(--navy);color:var(--white)}
.footer-brand{left:118px;top:124px;gap:10px}
.footer-brand .brand-mark{background:var(--white);width:28px;height:28px}
.footer-brand .brand-name{color:var(--white);font-size:13px;letter-spacing:.5px}
.footer-about{position:absolute;left:118px;top:178px;width:205px;font-size:10.5px;line-height:12.5px;text-align:justify}
.social{position:absolute;left:118px;top:245px;display:flex;gap:20px}
.social i{width:8px;height:8px;border-radius:50%;background:var(--sky)}
.foot-h{position:absolute;top:125px;font-family:'Montserrat',sans-serif;font-weight:600;font-size:16px;color:var(--sky)}
.links{position:absolute;left:393px;top:162px;list-style:none}
.links li{font-size:13px;line-height:24px;display:flex;align-items:center;gap:12px}
.links li::before{content:"";width:6px;height:6px;border-radius:50%;background:var(--sky)}
.contact-line{position:absolute;left:577px;display:flex;gap:10px;font-size:13px;line-height:16px}
.mini-post{position:absolute;left:832px;display:flex;gap:14px;width:260px}
.mini-thumb{flex:none;width:62px;height:44px;background:linear-gradient(180deg,#3b4a66,#8a6f55)}
.mini-post p{font-size:12.5px;line-height:15px}
.mini-post small{display:block;font-size:8px;font-weight:700;margin-top:5px}
.copyright{position:absolute;left:0;top:4590px;width:1200px;height:40px;background:#474747;color:#eee;font-size:12px;text-align:center;line-height:40px}
</style>
</head>
<body>

<header class="site-header">
  <div class="abs brand header-brand"><span class="brand-mark"></span><span class="brand-name">Harbor Crest Advisory</span></div>
  <div class="abs call">
    <span class="call-icon"><svg width="14" height="14" viewBox="0 0 24 24"><path fill="#fff" d="M6.6 10.8a15 15 0 0 0 6.6 6.6l2.2-2.2c.3-.3.7-.4 1-.2 1.1.4 2.3.6 3.6.6.6 0 1 .4 1 1V20c0 .6-.4 1-1 1A17 17 0 0 1 3 4c0-.6.4-1 1-1h3.5c.6 0 1 .4 1 1 0 1.3.2 2.5.6 3.6.1.3 0 .7-.2 1z"/></svg></span>
    <div><small>Call Us Now</small><strong>+ (503) 555-0148</strong></div>
  </div>
  <a class="abs login" href="#">LOGIN</a>
</header>

<nav class="main-nav">
  <a class="active" href="#" style="left:78px">HOME</a>
  <a href="#" style="left:264px">ABOUT US</a>
  <a href="#" style="left:462px">SERVICES</a>
  <a href="#" style="left:626px">OUR TEAM</a>
  <a href="#" style="left:842px">BLOG</a>
  <a href="#" style="left:1012px">CONTACT US</a>
</nav>

<section class="hero">
  <div class="hero-photo" role="img" aria-label="Photo of two advisors in suits reviewing documents at a laptop on an office desk"></div>
  <h1>Welcome to<br>Harbor Crest Advisory</h1>
  <p>We are a professional services organization with expertise in a comprehensive array of financial advisory and consulting services.</p>
  <a class="btn" href="#">Get Started</a>
</section>

<section class="advisory">
  <h2><em>Get</em> Financial Advisory<br>&amp; Valuation Services <em>Now</em></h2>
  <div class="copy">
    <p>Quid iudicant sensus? Quae qui non vident, nihil umquam magnum ac cognitione dignum amaverunt. Dicet pro me ipsa virtus nec dubitabit isti vestro beato M. Nihil ad rem! Ne sit sane;</p>
    <p>dicas, ipsae res verba rapiunt; Hoc non est positum in nostra actione. Quod ea non occurrentia fingunt, vincunt Aristonem; Haec para/doca illi, nos admirabilia dicamus. Et quidem, inquit, vehementer errat; Quarum ambarum rerum</p>
  </div>
  <div class="field" style="top:105px">Name <sup>*</sup></div>
  <div class="field" style="top:149px">Email <sup>*</sup></div>
  <div class="field" style="top:193px">Subject</div>
  <div class="field" style="top:240px;height:92px;width:348px">Message</div>
  <a class="btn" href="#">Send</a>
</section>

<section class="services">
  <h2 class="sec-title" style="top:84px">OUR <span>SERVICES</span></h2>
  <div class="rule" style="top:130px"></div>
  <p class="intro">Per porro dolore nostro, partem integre corpora per ea, tation ornatus mel ad. Brute voluptatibus an est, per cu utroque torquatos, ei eum amet hinc. Ne vis ludus timeam definitionem. His hinc dicunt minimum cu, qui te dico laoreet. Sea ea mucius diceret soleres, eos ei nostrud appellantur, an autem vocent novum doctus id mel. Id everti commune accusata meliore explicabo. Nemo enim ipsam voluptatem quia voluptas sit aspernatur aut odit aut fugit, sit aspernatur aut odit aut fugit.</p>

  <svg class="abs" style="left:0;top:0" width="1200" height="888" viewBox="0 0 1200 888">
    <g stroke="#0b2463" stroke-width="3" fill="none">
      <line x1="592" y1="400" x2="592" y2="460"/>
      <line x1="480" y1="560" x2="420" y2="520"/>
      <line x1="700" y1="560" x2="765" y2="520"/>
      <line x1="655" y1="660" x2="705" y2="705"/>
      <line x1="530" y1="660" x2="475" y2="705"/>
    </g>
    <g fill="#0b2463">
      <circle cx="592" cy="400" r="4"/><circle cx="420" cy="520" r="4"/><circle cx="765" cy="520" r="4"/>
      <circle cx="705" cy="705" r="4"/><circle cx="475" cy="705" r="4"/>
    </g>
    <circle cx="592" cy="575" r="108" fill="#0b2463"/>
    <circle cx="592" cy="575" r="78" fill="#fff"/>
    <circle cx="592" cy="575" r="50" fill="#0555a3"/>
    <g fill="#d5dbe4" stroke="#0b2463" stroke-width="1.5">
      <rect x="570" y="325" width="44" height="48" rx="3" role="img" aria-label="Legal document and gavel icon"/>
      <rect x="358" y="495" width="44" height="52" rx="3" role="img" aria-label="Tax form icon"/>
      <rect x="782" y="470" width="58" height="50" rx="3" role="img" aria-label="Coins and growing plant icon"/>
      <rect x="725" y="668" width="60" height="56" rx="3" role="img" aria-label="Hand holding rising chart icon"/>
      <rect x="400" y="708" width="58" height="56" rx="3" role="img" aria-label="Hand holding money icon"/>
    </g>
  </svg>

  <div class="svc" style="left:462px;top:263px;text-align:center;width:260px">LEGAL &amp;<span>BUSINESS STRUCTURING</span></div>
  <div class="svc" style="left:130px;top:495px;width:205px;text-align:right">TAX EFFICIENT<span>STRATEGIES</span></div>
  <div class="svc" style="left:858px;top:480px">LEVERAGE &amp;<span>FINANCING</span></div>
  <div class="svc" style="left:800px;top:680px">RISK MANAGEMENT &amp;<span>ASSET PROTECTION.</span></div>
  <div class="svc" style="left:150px;top:725px;width:238px;text-align:right">ASSET MANAGEMENT<span>&amp; INVESTING</span></div>
</section>

<section class="different">
  <div class="diff-panel">
    <h2>What make us<strong>DIFFERENT</strong></h2>
    <ul class="checks">
      <li><svg width="18" height="18" viewBox="0 0 18 18"><circle cx="9" cy="9" r="8" fill="none" stroke="#1c8ad6" stroke-width="1.4"/><path d="M5 9.3l2.6 2.5L13 6.5" fill="none" stroke="#1c8ad6" stroke-width="1.5"/></svg><span>constructio interrete. Quia nec<br>honesto quic quam</span></li>
      <li><svg width="18" height="18" viewBox="0 0 18 18"><circle cx="9" cy="9" r="8" fill="none" stroke="#1c8ad6" stroke-width="1.4"/><path d="M5 9.3l2.6 2.5L13 6.5" fill="none" stroke="#1c8ad6" stroke-width="1.5"/></svg><span>Dicet pro me ipsa virtus nec dubitabit</span></li>
      <li><svg width="18" height="18" viewBox="0 0 18 18"><circle cx="9" cy="9" r="8" fill="none" stroke="#1c8ad6" stroke-width="1.4"/><path d="M5 9.3l2.6 2.5L13 6.5" fill="none" stroke="#1c8ad6" stroke-width="1.5"/></svg><span>Hoc non est positum in nostra</span></li>
      <li><svg width="18" height="18" viewBox="0 0 18 18"><circle cx="9" cy="9" r="8" fill="none" stroke="#1c8ad6" stroke-width="1.4"/><path d="M5 9.3l2.6 2.5L13 6.5" fill="none" stroke="#1c8ad6" stroke-width="1.5"/></svg><span>Democriteum puto. Respondeat totidem verbis</span></li>
      <li><svg width="18" height="18" viewBox="0 0 18 18"><circle cx="9" cy="9" r="8" fill="none" stroke="#1c8ad6" stroke-width="1.4"/><path d="M5 9.3l2.6 2.5L13 6.5" fill="none" stroke="#1c8ad6" stroke-width="1.5"/></svg><span>Varietates autem iniurasque</span></li>
      <li><svg width="18" height="18" viewBox="0 0 18 18"><circle cx="9" cy="9" r="8" fill="none" stroke="#1c8ad6" stroke-width="1.4"/><path d="M5 9.3l2.6 2.5L13 6.5" fill="none" stroke="#1c8ad6" stroke-width="1.5"/></svg><span>Eae non sunt in potestate</span></li>
      <li><svg width="18" height="18" viewBox="0 0 18 18"><circle cx="9" cy="9" r="8" fill="none" stroke="#1c8ad6" stroke-width="1.4"/><path d="M5 9.3l2.6 2.5L13 6.5" fill="none" stroke="#1c8ad6" stroke-width="1.5"/></svg><span>Dignum amaverunt</span></li>
      <li><svg width="18" height="18" viewBox="0 0 18 18"><circle cx="9" cy="9" r="8" fill="none" stroke="#1c8ad6" stroke-width="1.4"/><path d="M5 9.3l2.6 2.5L13 6.5" fill="none" stroke="#1c8ad6" stroke-width="1.5"/></svg><span>Verum tamen cum de rebus grandioribus dicas</span></li>
      <li><svg width="18" height="18" viewBox="0 0 18 18"><circle cx="9" cy="9" r="8" fill="none" stroke="#1c8ad6" stroke-width="1.4"/><path d="M5 9.3l2.6 2.5L13 6.5" fill="none" stroke="#1c8ad6" stroke-width="1.5"/></svg><span>Nemo igitur esse beatus potest</span></li>
    </ul>
  </div>
  <div class="diff-photo" role="img" aria-label="Photo of a confident advisor in a suit seated at a laptop with hands clasped"></div>
</section>

<section class="team">
  <h2 class="sec-title" style="top:90px">OUR <span>TEAM</span></h2>
  <div class="rule" style="top:137px"></div>

  <div class="member-name" style="left:250px;top:188px;width:200px;text-align:right">MARCUS HALE</div>
  <p class="member-bio" style="left:165px;top:210px;text-align:right">Marcus Hale is the CFO and Strategist for our closely held businesses. As a former CPA, he takes in-depth roles in closely held companies as a financial consultant during times of exit or transition</p>
  <div class="more" style="left:390px;top:286px">READ MORE &#8594;</div>

  <div class="member-name" style="left:767px;top:188px">GRANT ELLISON</div>
  <p class="member-bio" style="left:767px;top:210px">Grant Ellison is the Financial Strategist and Founder who partners with C-Suite Executives, Family Offices, Real Estate Investors and Closely Held Business Owners to protect and maximize their wealth.</p>
  <div class="more" style="left:767px;top:286px">READ MORE &#8594;</div>

  <div class="abs" style="left:470px;top:172px;width:122px;height:122px;border-radius:50%;border:4px solid var(--navy);background:linear-gradient(180deg,#9fb4c7,#3d5a8a)" role="img" aria-label="Portrait photo of team member Marcus Hale"></div>
  <div class="abs" style="left:625px;top:172px;width:122px;height:122px;border-radius:50%;border:4px solid var(--navy);background:linear-gradient(180deg,#8aa07a,#3e4a5c)" role="img" aria-label="Portrait photo of team member Grant Ellison"></div>
</section>

<section class="testimonials">
  <div class="kicker" style="top:63px">TESTMONIALS</div>
  <h2 class="sec-head" style="top:80px">What Our Client Say</h2>

  <div class="arrow-btn" style="left:56px;top:283px"><svg width="8" height="10" viewBox="0 0 8 10"><path d="M6 1L2 5l4 4" fill="none" stroke="#fff" stroke-width="1.4"/></svg></div>
  <div class="arrow-btn" style="left:1105px;top:283px"><svg width="8" height="10" viewBox="0 0 8 10"><path d="M2 1l4 4-4 4" fill="none" stroke="#fff" stroke-width="1.4"/></svg></div>

  <div class="quote" style="left:208px;top:200px;width:229px;height:163px">
    <p style="padding:57px 20px 0">Grandioribus quibus rebus efficiuntur voluptates, eae non sunt in potestate sapientum.</p>
    <b style="top:130px">NORA FINCH</b>
  </div>
  <div class="quote" style="left:460px;top:190px;width:262px;height:190px">
    <p style="padding:57px 38px 0">Democriteumquibus rebus efficiuntur voluptates, eae non sunt in potestate sapientum Huicmorioptimum essepr Democriteumopterdesperanon</p>
    <b style="top:150px">HELEN</b>
  </div>
  <div class="quote" style="left:748px;top:200px;width:227px;height:163px">
    <p style="padding:57px 24px 0">Nam quibus rebus efficiuntur voluptates, eae non sunt in potestate sapientiumHuic mori optimum esse propter</p>
    <b style="top:130px">PORTER</b>
  </div>

  <div class="avatar" style="left:289px;top:175px;width:64px;height:64px" role="img" aria-label="Client photo of Nora Finch"></div>
  <div class="avatar" style="left:555px;top:162px;width:70px;height:70px" role="img" aria-label="Client photo of Helen"></div>
  <div class="avatar" style="left:828px;top:175px;width:64px;height:64px;background:linear-gradient(180deg,#c4cfdc,#4a5c7a)" role="img" aria-label="Client photo of Porter"></div>
</section>
<span class="dot" style="left:567px;background:var(--blue)"></span>
<span class="dot" style="left:588px"></span>
<span class="dot" style="left:609px"></span>

<section class="blog">
  <div class="kicker" style="top:83px">OUR BLOG</div>
  <h2 class="sec-head" style="top:102px">Latest Articles</h2>

  <article class="post" style="left:125px">
    <div class="post-photo" role="img" aria-label="Photo of a timber lodge style building with peaked roofs" style="background:linear-gradient(180deg,#c9d2dc 0%,#8f8a82 55%,#4d4a47 100%)"></div>
    <div class="meta">By Admin | 4 January 2021</div>
    <h3>Efficiuntur Volupt<br>Nostra Actione</h3>
    <p>Philosophi autem in suis lectulis plerumque moriuntur. Paulum, cum regem Persem captum adduceret, eodem flumine lectulis plerumque moriunturin-vectioPaulum,Persem</p>
    <div class="more">READ MORE &#10230;</div>
  </article>

  <article class="post" style="left:608px">
    <div class="post-photo" role="img" aria-label="Photo of a lit townhouse street at dusk" style="background:linear-gradient(180deg,#4c6087 0%,#7a6e77 45%,#8a5a3e 80%,#3a2e2a 100%)"></div>
    <div class="meta">By Admin | 4 January 2021</div>
    <h3>Plerumque Ptates<br>Eae Non sunt In</h3>
    <p>Beatus potest autem in suis lectulis plerumque moriuntur. Paulum, cum regem Persem captum adduceret, eodem flumine lectulis plerumque morionturinvectilum,Persem</p>
    <div class="more">READ MORE &#10230;</div>
  </article>
</section>

<footer class="site-footer">
  <div class="abs brand footer-brand"><span class="brand-mark"></span><span class="brand-name">Harbor Crest Advisory</span></div>
  <p class="footer-about">quaerimus, qualis Q. Nam quibus rebus efficiuntur voluptates, eae non sunt in potestate sapientis. Negare non possum. Huic mori optimum esse propter desperationem sapientiae,</p>
  <div class="social"><i></i><i></i><i></i><i></i><i></i></div>

  <div class="foot-h" style="left:390px">QUICK LINK</div>
  <ul class="links">
    <li>Links</li><li>Home</li><li>About us</li><li>Services</li><li>Our team</li><li>Contact us</li>
  </ul>

  <div class="foot-h" style="left:577px">CONTACT US</div>
  <div class="contact-line" style="top:168px"><svg width="10" height="14" viewBox="0 0 10 14"><path d="M5 0a5 5 0 0 0-5 5c0 4 5 9 5 9s5-5 5-9a5 5 0 0 0-5-5zm0 7a2 2 0 1 1 0-4 2 2 0 0 1 0 4z" fill="#1c8ad6"/></svg><span>847 W Alder Ln, Suite 412,<br>Fernhollow, WA 98915</span></div>
  <div class="contact-line" style="top:228px"><svg width="10" height="12" viewBox="0 0 24 24"><path fill="#1c8ad6" d="M6.6 10.8a15 15 0 0 0 6.6 6.6l2.2-2.2c.3-.3.7-.4 1-.2 1.1.4 2.3.6 3.6.6.6 0 1 .4 1 1V20c0 .6-.4 1-1 1A17 17 0 0 1 3 4c0-.6.4-1 1-1h3.5c.6 0 1 .4 1 1 0 1.3.2 2.5.6 3.6.1.3 0 .7-.2 1z"/></svg><span>503-555-0172</span></div>
  <div class="contact-line" style="top:245px"><svg width="10" height="12" viewBox="0 0 10 8"><rect x=".5" y=".5" width="9" height="7" fill="none" stroke="#1c8ad6"/><path d="M.5.5L5 4.5 9.5.5" fill="none" stroke="#1c8ad6"/></svg><span>info@harborcrestadvisory.com</span></div>
  <div class="contact-line" style="top:262px"><svg width="10" height="12" viewBox="0 0 10 10"><circle cx="5" cy="5" r="4.5" fill="none" stroke="#1c8ad6"/></svg><span>www.harborcrestadvisory.com</span></div>

  <div class="foot-h" style="left:830px">OUR BLOGS</div>
  <div class="mini-post" style="top:168px"><div class="mini-thumb" role="img" aria-label="Thumbnail photo of a townhouse street"></div><p>luxuriae licentiam quaque, aliter in vita? Non igitur de<small>April 19, 2020</small></p></div>
  <div class="mini-post" style="top:248px"><div class="mini-thumb" role="img" aria-label="Thumbnail photo of a timber lodge" style="background:linear-gradient(180deg,#c9d2dc,#5a5550)"></div><p>An hoc usque quaque, aliter in vita? Non igitur de<small>March 19, 2020</small></p></div>
</footer>
<div class="copyright">Copyright&copy;2021, Bramblefield Co. All Right Reserved</div>

</body>
</html>
```